Redesign Website - Current one too plain

The description is in the uploaded file. Please let me know if you need any more information. I'd prefer it if someone could implement the design to a WordPress site but the best design will win, regardless.
I would like the forms to look nice as well
UPDATE:
I don't think we can use the images that I provided, I think they make the site look a bit 'cheap' and I really don't know how to replace them. One thought I have had is to make the "Simple, Unique, Effective" a second feature on the right side of the page with the search on the left
Target Market(s)
Small companies, private sellers of cars and people who rent their caravan/holiday home out
Industry/Entity Type
Advertising
Number of Pages Required
3 page
Colors
Designer to choose colors to be used in the design.
Look and feel

```html
<!DOCTYPE html>
<html lang="en">
<head>
<meta charset="utf-8">
<title>Kodra – Discover And Connect</title>
<link href="https://fonts.googleapis.com/css2?family=Inter:wght@400;500;600;700&display=swap" rel="stylesheet">
<style>
  :root {
    --ink: #222222;
    --lime: #e9fb52;
    --white: #ffffff;
    --text-dark: #1a1a1a;
    --photo-light: #d3cfc8;
    --photo-mid: #a9a6a1;
    --photo-dark: #55585c;
  }
  * { margin: 0; padding: 0; box-sizing: border-box; }
  html, body { width: 1200px; height: 2853px; overflow: hidden; }
  body {
    position: relative;
    background: var(--ink);
    color: var(--white);
    font-family: "Inter", Arial, sans-serif;
  }
  .abs { position: absolute; }

  /* Header */
  .brand { left: 85px; top: 36px; display: flex; align-items: center; gap: 10px; color: var(--lime); font-size: 22px; font-weight: 500; }
  .brand-dot { width: 28px; height: 28px; border-radius: 50%; background: var(--lime); }
  .main-nav { top: 43px; left: 0; width: 100%; }
  .main-nav a { position: absolute; color: var(--white); text-decoration: none; font-size: 13px; font-weight: 500; white-space: nowrap; }
  .btn-login { left: 977px; top: 35px; width: 137px; height: 36px; border-radius: 18px; background: var(--lime); color: var(--ink); font-size: 17px; font-weight: 500; display: flex; align-items: center; justify-content: center; }

  /* Hero */
  .hero-title { left: 0; width: 100%; top: 137px; text-align: center; font-size: 62px; font-weight: 700; letter-spacing: 0.5px; }
  .hero-sub { left: 0; width: 100%; top: 223px; text-align: center; font-size: 16px; }
  .code-digit { width: 60px; text-align: center; color: var(--lime); font-size: 80px; font-weight: 600; line-height: 1; }
  .chev { width: 16px; height: 16px; }
  .chip { top: 439px; height: 33px; border: 1.5px solid var(--lime); border-radius: 17px; color: var(--lime); font-size: 16px; display: flex; align-items: center; justify-content: center; }
  .btn-search { left: 481px; top: 500px; width: 237px; height: 36px; border-radius: 18px; background: var(--lime); color: var(--ink); font-size: 16px; font-weight: 500; display: flex; align-items: center; justify-content: center; }
  .hero-photo { left: 160px; top: 612px; width: 860px; height: 220px; border-radius: 18px 18px 0 0; background: linear-gradient(180deg, var(--photo-dark) 0%, var(--photo-light) 30%, var(--photo-mid) 100%); }

  /* About */
  .about-panel { left: 57px; top: 822px; width: 1086px; height: 480px; background: var(--white); border-radius: 22px; }
  .about-title { left: 0; width: 100%; top: 884px; text-align: center; color: var(--text-dark); font-size: 26px; font-weight: 600; }
  .feature-card { top: 975px; width: 267px; height: 266px; background: var(--ink); border-radius: 26px; text-align: center; }
  .feature-icon { position: absolute; left: 50%; top: 52px; transform: translateX(-50%); width: 80px; height: 80px; }
  .feature-name { position: absolute; left: 0; width: 100%; top: 152px; color: var(--lime); font-size: 21px; font-weight: 600; }
  .feature-text { position: absolute; left: 30px; right: 30px; top: 186px; font-size: 13px; line-height: 16px; }
  .feature-text.narrow { left: 38px; right: 38px; }

  /* Why choose us */
  .why-band { left: 0; top: 1427px; width: 1200px; height: 396px; background: var(--lime); color: var(--text-dark); }
  .why-title { position: absolute; left: 0; width: 100%; top: 49px; text-align: center; font-size: 26px; font-weight: 600; }
  .why-body { position: absolute; left: 72px; width: 1060px; top: 142px; font-size: 17px; line-height: 28.4px; }
  .why-body ul { padding-left: 26px; }

  /* How it works */
  .fleet-photo { left: 65px; top: 1885px; width: 1040px; height: 340px; border-radius: 40px 40px 60px 60px; background: linear-gradient(180deg, #4a4c50 0%, #cfcbc4 30%, #a9a9a9 70%, #3a3a3a 100%); }
  .how-title { left: 0; width: 100%; top: 2274px; text-align: center; color: var(--lime); font-size: 26px; font-weight: 600; }
  .steps { left: 60px; width: 1080px; top: 2367px; font-size: 17px; line-height: 28.4px; }
  .step { margin-bottom: 28px; }
</style>
</head>
<body>

<header>
  <div class="abs brand"><span class="brand-dot"></span><span>Kodra</span></div>
  <nav class="abs main-nav">
    <a style="left:410px">Home</a>
    <a style="left:486px">Advertise</a>
    <a style="left:592px">Contact</a>
    <a style="left:697px">Register</a>
  </nav>
  <div class="abs btn-login">Login</div>
</header>

<section class="hero">
  <h1 class="abs hero-title">Discover And Connect</h1>
  <p class="abs hero-sub">Display Your Unique Code on Your Vehicle to Attract Customers</p>

  <svg class="abs chev" style="left:538px;top:292px" viewBox="0 0 16 16"><circle cx="8" cy="8" r="8" fill="var(--lime)"/><path d="M4.5 9.5 8 6l3.5 3.5" stroke="var(--ink)" stroke-width="1.6" fill="none"/></svg>
  <svg class="abs chev" style="left:623px;top:292px" viewBox="0 0 16 16"><circle cx="8" cy="8" r="8" fill="var(--lime)"/><path d="M4.5 9.5 8 6l3.5 3.5" stroke="var(--ink)" stroke-width="1.6" fill="none"/></svg>
  <div class="abs code-digit" style="left:516px;top:312px">S</div>
  <div class="abs code-digit" style="left:601px;top:312px">6</div>
  <svg class="abs chev" style="left:538px;top:394px" viewBox="0 0 16 16"><circle cx="8" cy="8" r="8" fill="var(--lime)"/><path d="M4.5 6.5 8 10l3.5-3.5" stroke="var(--ink)" stroke-width="1.6" fill="none"/></svg>
  <svg class="abs chev" style="left:623px;top:394px" viewBox="0 0 16 16"><circle cx="8" cy="8" r="8" fill="var(--lime)"/><path d="M4.5 6.5 8 10l3.5-3.5" stroke="var(--ink)" stroke-width="1.6" fill="none"/></svg>

  <div class="abs chip" style="left:439px;width:55px">Car</div>
  <div class="abs chip" style="left:529px;width:93px">Caravan</div>
  <div class="abs chip" style="left:657px;width:104px">Company</div>
  <div class="abs btn-search">Search</div>

  <div class="abs hero-photo" role="img" aria-label="Photo of a static caravan holiday home"></div>
</section>

<section>
  <div class="abs about-panel"></div>
  <h2 class="abs about-title">About us</h2>

  <div class="abs feature-card" style="left:133px">
    <div class="feature-icon" role="img" aria-label="Hand snapping fingers icon" style="width:44px;height:76px;border-radius:20px;background:var(--lime);opacity:.85"></div>
    <div class="feature-name">Simple</div>
    <p class="feature-text">Create your advert and display your code</p>
  </div>

  <div class="abs feature-card" style="left:467px">
    <svg class="feature-icon" viewBox="0 0 80 80" fill="none" stroke="var(--lime)" stroke-width="2.5">
      <circle cx="30" cy="30" r="22"/><circle cx="30" cy="30" r="14"/><circle cx="30" cy="30" r="6"/>
      <circle cx="48" cy="48" r="14" fill="var(--ink)"/><path d="M58 58l12 12"/>
    </svg>
    <div class="feature-name" style="top:150px">Unique</div>
    <p class="feature-text" style="top:184px">Customers find you by an easy-to-remember code</p>
  </div>

  <div class="abs feature-card" style="left:800px">
    <svg class="feature-icon" viewBox="0 0 80 80" fill="none" stroke="var(--lime)" stroke-width="2.5">
      <circle cx="40" cy="40" r="36"/><circle cx="40" cy="40" r="24" stroke-dasharray="6 3"/><circle cx="40" cy="40" r="14"/>
      <path d="M40 32v8l5 4"/>
    </svg>
    <div class="feature-name" style="top:149px">Effective</div>
    <p class="feature-text narrow" style="top:183px">Customers are directed to you and not a list of your competitors</p>
  </div>
</section>

<section class="abs why-band">
  <h2 class="why-title">Why Choose Us</h2>
  <div class="why-body">
    <p>Our platform offers a user-friendly experience that empowers businesses of all sizes to increase their presence. With our easy-to-use system and eye-catching codes, you can enjoy these benefits:</p>
    <ul>
      <li>Stand out from competitors with a unique identifier</li>
      <li>Attract more customers with straightforward access to your business</li>
      <li>Increase your brand recognition and credibility</li>
      <li>Track the effectiveness of your adverts with real-time data</li>
    </ul>
  </div>
</section>

<section>
  <div class="abs fleet-photo" role="img" aria-label="Photo of a silver SUV, a static caravan and a liveried work van"></div>
  <h2 class="abs how-title">How it works</h2>
  <div class="abs steps">
    <div class="step"><p>Step 1:</p><p>Create Your Advert Content:</p><p>Generate your unique code and create an eye-catching advert that showcases your business. Highlight your products, services, and contact details to ensure customers can easily reach you.</p></div>
    <div class="step"><p>Step 2:</p><p>Display Your Code Content:</p><p>Affix your code prominently on your vehicles. Whether it's a car, van, or caravan, your code will act as a beacon, guiding interested customers right to your doorstep.</p></div>
    <div class="step"><p>Step 3:</p><p>Customers Find Your Content:</p><p>Sit back and watch as customers effortlessly find and connect with your business using your memorable code. Increase your visibility and enhance your customer base with our innovative concept.</p></div>
  </div>
</section>

</body>
</html>
```